Roadwise Beacon Traffic Control Company Website

Modern website Wordpress design using all greyscale photos with a pop of red (such as road closure signs or detour cones) for strategic emphasis. (see brand guide for color codes)
The creative goal is to leverage high-contrast, desaturated imagery to create a clean, professional, and industrial feel. The selective use of red will draw immediate attention to critical elements—such as road hazards, safety equipment, or key messages to ensure the viewer's focus is directed with purpose.

Brand guide, homepage content and logo are attached. Create clean professional user experience to market services to industry professionals.

```html
<!DOCTYPE html>
<html lang="en">
<head>
<meta charset="utf-8">
<title>Roadwise Beacon Traffic Control Company</title>
<link href="https://fonts.googleapis.com/css2?family=Poppins:ital,wght@0,300;0,400;0,500;0,600;0,700;0,800;1,400&display=swap" rel="stylesheet">
<style>
:root{
  --red:#ed1c24;
  --ink:#111111;
  --grey-text:#555555;
  --line:#e4e4e4;
  --backdrop:#e9e9e9;
  --white:#ffffff;
}
*{box-sizing:border-box;margin:0;padding:0}
html,body{width:1200px;height:993px;overflow:hidden;background:var(--backdrop);font-family:'Poppins',sans-serif;color:var(--ink)}
.page{position:absolute;left:355px;top:20px;width:769px;height:1495px;background:var(--white);transform:scale(0.6375);transform-origin:0 0;overflow:hidden}
.page > *{position:absolute}
.top-rule{left:0;top:0;width:769px;height:3px;background:var(--red)}
.brand{display:flex;align-items:center;gap:5px;font-weight:600;font-size:9px;color:var(--ink);white-space:nowrap}
.brand-mark{width:9px;height:9px;background:var(--red)}
.site-header .brand{left:22px;top:21px}
.main-nav{left:0;width:769px;top:22px}
.main-nav a{position:absolute;font-size:6.5px;color:var(--ink);text-decoration:none;letter-spacing:.2px}
.btn-contact{left:658px;top:15px;width:89px;height:22px;border-radius:11px;background:var(--red);color:var(--white);font-size:6.5px;display:flex;align-items:center;padding-left:9px}
.btn-contact .dot{position:absolute;right:3px;top:3px;width:16px;height:16px;border-radius:50%;background:var(--white);display:flex;align-items:center;justify-content:center}
.round-arrow{width:26px;height:26px;border-radius:50%;background:var(--red);display:flex;align-items:center;justify-content:center}
.hero{left:22px;top:51px;width:725px;height:394px}
.hero svg.bg{position:absolute;inset:0}
.hero-title{position:absolute;left:30px;top:212px;color:var(--white);font-weight:800;font-size:49px;line-height:38px;letter-spacing:-1px}
.hero-sub{position:absolute;left:32px;top:331px;color:var(--white);font-weight:400;font-size:24px;letter-spacing:-.4px}
.hero-note{position:absolute;right:28px;top:229px;width:108px;text-align:right;color:var(--white);font-size:8px;line-height:12.3px}
.hero-arrows{position:absolute;left:648px;top:357px;display:flex;gap:7px}
.intro-title{left:0;width:769px;top:518px;text-align:center;font-weight:600;font-size:29.5px;line-height:24px;letter-spacing:-.2px}
.intro-text{left:0;width:769px;top:591px;text-align:center;font-size:7.6px;line-height:12px;color:var(--grey-text)}
.divider{left:55px;top:660px;width:672px;height:1px;background:var(--line)}
.section-title{left:0;width:769px;top:710px;text-align:center;font-weight:600;font-size:29px}
.slider-arrows{left:354px;top:814px;display:flex;gap:7px}
.service-card{width:220px}
.service-photo{width:220px;height:241px;border-radius:10px}
.photo-cone{background:
  radial-gradient(ellipse 30% 45% at 48% 62%,rgba(90,90,90,.55),rgba(90,90,90,0) 70%),
  radial-gradient(ellipse 60% 30% at 50% 88%,#4e4e4e,rgba(78,78,78,0) 80%),
  linear-gradient(180deg,#d9d9d9 0%,#bdbdbd 30%,#8e8e8e 62%,#5c5c5c 100%)}
.photo-signs{background:
  radial-gradient(ellipse 45% 40% at 28% 55%,#3f3f3f,rgba(63,63,63,0) 75%),
  radial-gradient(ellipse 35% 35% at 45% 25%,#6a6a6a,rgba(106,106,106,0) 75%),
  radial-gradient(ellipse 30% 30% at 40% 88%,#505050,rgba(80,80,80,0) 75%),
  linear-gradient(120deg,#8a8a8a 0%,#b0b0b0 45%,#e2e2e2 75%,#d0d0d0 100%)}
.photo-car{background:
  radial-gradient(ellipse 55% 22% at 55% 55%,#2e2e2e,rgba(46,46,46,0) 85%),
  linear-gradient(180deg,#ececec 0%,#d2d2d2 30%,#7d7d7d 48%,#5e5e5e 62%,#8c8c8c 80%,#6a6a6a 100%)}
.service-name{font-weight:600;font-size:10.5px;line-height:15px;margin-top:14px}
.explore{display:flex;align-items:center;gap:7px;font-size:6.5px;font-weight:500;margin-top:9px}
.explore .round-arrow{width:15px;height:15px}
.footer{left:22px;top:1240px;width:725px;height:224px}
.footer svg.bg{position:absolute;inset:0}
.footer .brand{position:absolute;left:0;top:10px}
.footer-tag{position:absolute;left:0;width:725px;top:33px;text-align:center;color:var(--white);font-style:italic;font-size:10px}
.footer-list{position:absolute;top:66px;list-style:none;color:var(--white);font-size:7px}
.footer-list li{display:flex;align-items:center;gap:8px;height:19.3px}
.footer-rule{position:absolute;left:78px;top:164px;width:562px;height:1px;background:rgba(255,255,255,.35)}
.copyright{position:absolute;left:0;width:725px;top:191px;text-align:center;color:var(--white);font-size:7px}
</style>
</head>
<body>
<div class="page">
  <div class="top-rule"></div>

  <header class="site-header">
    <div class="brand" style="position:absolute"><span class="brand-mark"></span>Roadwise Beacon</div>
  </header>
  <nav class="main-nav">
    <a style="left:281px">HOME</a>
    <a style="left:323px">ABOUT</a>
    <a style="left:367px">SERVICES</a>
    <a style="left:420px">RENTALS</a>
    <a style="left:470px">JOBS</a>
  </nav>
  <a class="btn-contact">Contact Us Now
    <span class="dot"><svg width="8" height="8" viewBox="0 0 8 8"><path d="M2 6L6 2M3 2H6V5" stroke="#111" stroke-width="1" fill="none"/></svg></span>
  </a>

  <section class="hero">
    <svg class="bg" width="725" height="394" viewBox="0 0 725 394" role="img" aria-label="Greyscale photo of traffic signals with a right-turn arrow against blurred trees and buildings">
      <defs>
        <clipPath id="heroShape">
          <path d="M20,0 H705 Q725,0 725,20 V323 Q725,343 705,343 H648 Q628,343 628,363 V374 Q628,394 608,394 H20 Q0,394 0,374 V20 Q0,0 20,0 Z"/>
        </clipPath>
        <linearGradient id="heroSky" x1="0" y1="0" x2="0" y2="1">
          <stop offset="0" stop-color="#bdbdbd"/>
          <stop offset="0.45" stop-color="#d6d6d6"/>
          <stop offset="1" stop-color="#8a8a8a"/>
        </linearGradient>
        <radialGradient id="heroLeft" cx="0.08" cy="0.55" r="0.45">
          <stop offset="0" stop-color="#1e1e1e"/>
          <stop offset="0.6" stop-color="#2e2e2e" stop-opacity=".75"/>
          <stop offset="1" stop-color="#2e2e2e" stop-opacity="0"/>
        </radialGradient>
        <radialGradient id="heroRight" cx="0.95" cy="0.5" r="0.35">
          <stop offset="0" stop-color="#2a2a2a"/>
          <stop offset="0.6" stop-color="#3a3a3a" stop-opacity=".7"/>
          <stop offset="1" stop-color="#3a3a3a" stop-opacity="0"/>
        </radialGradient>
        <radialGradient id="heroCentre" cx="0.5" cy="0.55" r="0.22">
          <stop offset="0" stop-color="#252525" stop-opacity=".85"/>
          <stop offset="1" stop-color="#252525" stop-opacity="0"/>
        </radialGradient>
        <linearGradient id="heroFloor" x1="0" y1="0" x2="0" y2="1">
          <stop offset="0.55" stop-color="#111" stop-opacity="0"/>
          <stop offset="1" stop-color="#111" stop-opacity=".8"/>
        </linearGradient>
      </defs>
      <g clip-path="url(#heroShape)">
        <rect width="725" height="394" fill="url(#heroSky)"/>
        <rect width="725" height="394" fill="url(#heroLeft)"/>
        <rect width="725" height="394" fill="url(#heroRight)"/>
        <rect width="725" height="394" fill="url(#heroCentre)"/>
        <rect width="725" height="394" fill="url(#heroFloor)"/>
      </g>
    </svg>
    <h1 class="hero-title">TRAFFIC<br>CONTROL<br>SOLUTIONS</h1>
    <p class="hero-sub">ENGINEERED FOR SAFETY</p>
    <p class="hero-note">Lorem Ipsum is simply dummy text of the printing and typesetting industry. Lorem Ipsum has been the industry's</p>
    <div class="hero-arrows">
      <span class="round-arrow"><svg width="10" height="8" viewBox="0 0 10 8"><path d="M9 4H1M4 1L1 4L4 7" stroke="#fff" fill="none"/></svg></span>
      <span class="round-arrow"><svg width="10" height="8" viewBox="0 0 10 8"><path d="M1 4H9M6 1L9 4L6 7" stroke="#fff" fill="none"/></svg></span>
    </div>
  </section>

  <h2 class="intro-title">SAFETY ISN'T A PRIORITY, IT'S THE<br>FOUNDATION OF EVERYTHING WE DO</h2>
  <p class="intro-text">Lorem Ipsum is simply dummy text of the printing and typesetting industry. Lorem Ipsum has been<br>the industry's standard dummy text ever since the 1500s, when an unknown.</p>
  <div class="divider"></div>

  <h2 class="section-title">SERVICES</h2>
  <div class="slider-arrows">
    <span class="round-arrow" style="width:28px;height:28px"><svg width="10" height="8" viewBox="0 0 10 8"><path d="M9 4H1M4 1L1 4L4 7" stroke="#fff" fill="none"/></svg></span>
    <span class="round-arrow" style="width:28px;height:28px"><svg width="10" height="8" viewBox="0 0 10 8"><path d="M1 4H9M6 1L9 4L6 7" stroke="#fff" fill="none"/></svg></span>
  </div>

  <article class="service-card" style="left:43px;top:818px">
    <div class="service-photo photo-cone" role="img" aria-label="Greyscale photo of a traffic cone on an asphalt road"></div>
    <h3 class="service-name">Flagging &amp; Lane Closures</h3>
    <a class="explore">Explore More <span class="round-arrow"><svg width="7" height="7" viewBox="0 0 8 8"><path d="M2 6L6 2M3 2H6V5" stroke="#fff" fill="none"/></svg></span></a>
  </article>

  <article class="service-card" style="left:274px;top:874px">
    <div class="service-photo photo-signs" role="img" aria-label="Greyscale photo of a pile of road signs"></div>
    <h3 class="service-name">Temporary Traffic Control Plans<br>(TTCPs)</h3>
    <a class="explore">Explore More <span class="round-arrow"><svg width="7" height="7" viewBox="0 0 8 8"><path d="M2 6L6 2M3 2H6V5" stroke="#fff" fill="none"/></svg></span></a>
  </article>

  <article class="service-card" style="left:506px;top:818px">
    <div class="service-photo photo-car" role="img" aria-label="Greyscale photo of a car driving on a road"></div>
    <h3 class="service-name">Signage &amp; Barricades</h3>
    <a class="explore">Explore More <span class="round-arrow"><svg width="7" height="7" viewBox="0 0 8 8"><path d="M2 6L6 2M3 2H6V5" stroke="#fff" fill="none"/></svg></span></a>
  </article>

  <footer class="footer">
    <svg class="bg" width="725" height="224" viewBox="0 0 725 224" aria-hidden="true">
      <path d="M81,0 H705 Q725,0 725,20 V162 Q725,182 705,182 H702 Q682,182 682,202 V204 Q682,224 662,224 H20 Q0,224 0,204 V72 Q0,52 20,52 H41 Q61,52 61,32 V20 Q61,0 81,0 Z" fill="#ed1c24"/>
    </svg>
    <div class="brand"><span class="brand-mark"></span>Roadwise Beacon</div>
    <p class="footer-tag">Serving Texas Industry to Ensure Safety, Compliance, and Efficient Traffic Flow</p>
    <ul class="footer-list" style="left:170px">
      <li><svg width="11" height="9" viewBox="0 0 11 9"><path d="M1 5L4 8L10 1" stroke="#fff" stroke-width="1.4" fill="none"/></svg>Road construction, maintenance, &amp; Detours</li>
      <li><svg width="11" height="9" viewBox="0 0 11 9"><path d="M1 5L4 8L10 1" stroke="#fff" stroke-width="1.4" fill="none"/></svg>Municipal &amp; State projects</li>
      <li><svg width="11" height="9" viewBox="0 0 11 9"><path d="M1 5L4 8L10 1" stroke="#fff" stroke-width="1.4" fill="none"/></svg>Private Sector &amp; Commercial Contractors</li>
      <li><svg width="11" height="9" viewBox="0 0 11 9"><path d="M1 5L4 8L10 1" stroke="#fff" stroke-width="1.4" fill="none"/></svg>Oil, Gas, Wind, Solar, &amp; Manufacturing</li>
    </ul>
    <ul class="footer-list" style="left:406px">
      <li><svg width="11" height="9" viewBox="0 0 11 9"><path d="M1 5L4 8L10 1" stroke="#fff" stroke-width="1.4" fill="none"/></svg>State DOT-Compliant &amp; Certified</li>
      <li><svg width="11" height="9" viewBox="0 0 11 9"><path d="M1 5L4 8L10 1" stroke="#fff" stroke-width="1.4" fill="none"/></svg>Experienced &amp; Trained Crew</li>
      <li><svg width="11" height="9" viewBox="0 0 11 9"><path d="M1 5L4 8L10 1" stroke="#fff" stroke-width="1.4" fill="none"/></svg>Reliable &amp; Responsive</li>
      <li><svg width="11" height="9" viewBox="0 0 11 9"><path d="M1 5L4 8L10 1" stroke="#fff" stroke-width="1.4" fill="none"/></svg>Cost-Effective &amp; Efficient</li>
    </ul>
    <div class="footer-rule"></div>
    <p class="copyright">Copyright © 2025 Roadwise Beacon. All Rights Reserved.</p>
  </footer>
</div>
</body>
</html>
```